Accountant website

Please design a accountant website for www.quillbrookadvisory.com.au. This site is majorly out of date, and is not supported by modern browsers.

The style should use the reds from the design at dev.quillbrookadvisory.com.au, and should be modern and make use of Slides (large content slides that the user scrolls through on the front page).

The content is largely already on the site, however happy to move some around to suit the modern design as required.

The dev.quillbrookadvisory.com.au was a rough mock up that I have completed that the client is "happy" with the direction, however this needs a lot of polish and finishing touches, and I will accept designs that differ from this, but highly recommend that this is used as a guide.

Ready to be sliced PSD Only - HTML no required.

In all honesty, although I can technically do a lot of this, the polished finished I want for this site has eluded me in a few attempts, and therefore I am looking out there at you much more artistic people to finish (or redesign if required) this site.

Target Market(s)

Higher end Small - Medium Business

Industry/Entity Type

Accountant

Requirements
Must have
• Must use the logo from dev.quillbrookadvisory.com.au use exactly the red colours as defined in this layout. A basic layout PSD (to get the colour etc) and the logo in ai format is attached to this project. Please ignore the SSL warning on the development site.

The final product does NOT have to be the same as shown on dev.quillbrookadvisory.com.au however the red colour scheme must be used. The client DOES want the logo on the RIGHT.

Must have a front landing page design, and a page layout that considers the other page content (at least one separate PSD)
Nice to have
• I really am looking at a slide format for the front page simular to:

http://www.plumvane.com/au/
http://www.tessaform.com/

The attached photos should be used on the site. Was considering a rotating banner with these images are a watermark background on a solid Red header bar, but happy to be shown other options.
Should not have
• Please no "Layout Goblin" submissions.

```html
<!DOCTYPE html>
<html lang="en">
<head>
<meta charset="utf-8">
<title>Quillbrook Advisory</title>
<link href="https://fonts.googleapis.com/css2?family=PT+Sans+Narrow:wght@400;700&family=PT+Sans:wght@700&family=Arimo:wght@400;700&display=swap" rel="stylesheet">
<style>
:root{
  --red:#c8262c;
  --red-dark:#a91e23;
  --ink:#1c1c1c;
  --text:#333;
  --muted:#555;
  --footer:#2b2b2b;
  --footer-base:#1f1f1f;
  --footer-text:#cfcfcf;
  --footer-head:#a9a9a9;
  --rule:#e2e2e2;
  --icon:#ececec;
}
*{margin:0;padding:0;box-sizing:border-box}
html,body{width:914px;height:1200px;overflow:hidden;background:#fff}
body{position:relative;font-family:"Arimo",Arial,sans-serif;color:var(--text)}
.abs{position:absolute}

/* header: utilities left, brand right */
.brand{right:108px;top:30px;text-align:right;font-family:"PT Sans Narrow",sans-serif;font-weight:700;color:var(--ink);font-size:32px;line-height:30px;letter-spacing:.5px}
.brand small{display:block;font-size:12.5px;line-height:16px;font-weight:400;letter-spacing:.3px}
.account-links{left:108px;top:24px;font-family:"PT Sans Narrow",sans-serif;font-weight:700;font-size:11px;color:var(--red)}
.account-links i{font-style:normal;margin:0 4px}
.lang{left:108px;top:62px;width:80px;height:20px;background:#eee;border:1px solid #ddd;font-size:7px;color:#555;display:flex;align-items:center;padding-left:4px}
.lang .flag{width:13px;height:9px;background:#2b3f8c;margin-right:5px}
.lang .caret{margin-left:auto;width:14px;border-left:1px solid #ccc;height:100%;display:flex;align-items:center;justify-content:center}
.search{left:197px;top:62px;width:115px;height:20px;background:#e9e9e9;font-size:9px;color:#444;padding:4px 7px}
.search svg{position:absolute;right:6px;top:5px}

/* nav */
.mainnav{left:0;top:109px;width:914px;height:28px;background:linear-gradient(#e0353b,var(--red-dark))}
.mainnav a{position:absolute;top:9px;font-family:"PT Sans Narrow",sans-serif;font-weight:700;font-size:10px;color:#fff;text-decoration:none}

/* hero */
.hero{left:0;top:137px;width:914px;height:327px;background:linear-gradient(100deg,#b9b19c 0%,#cfc6ad 35%,#8a7a5c 60%,#6f8b4a 85%,#5b7a3c 100%)}
.hero-title{left:186px;top:250px;font-family:"PT Sans",sans-serif;font-weight:700;font-size:34px;line-height:52px;color:#111;text-shadow:0 0 6px rgba(255,255,255,.9)}
.hero-title span{display:block;padding-left:8px}
.dots{left:254px;top:408px;display:flex;gap:3px}
.dots b{width:9px;height:9px;border-radius:50%;background:#222}
.dots b:first-child{background:var(--red)}

/* intro */
.section-head{font-family:"PT Sans Narrow",sans-serif;font-weight:700;font-size:12px;color:var(--red);text-transform:uppercase}
.intro-text{left:108px;top:516px;width:570px;font-size:10.3px;line-height:17.6px;color:#111}
.btn{background:linear-gradient(#4a4a4a,#2e2e2e);color:#fff;font-family:"PT Sans Narrow",sans-serif;font-weight:700;display:flex;align-items:center;justify-content:center;border-radius:4px}

/* columns */
.photo{left:108px;top:606px;width:306px;height:131px;background:linear-gradient(90deg,#6e8aa8,#b8c2c8 50%,#9a9f98);border:1px solid #ccc}
.diff-text{left:108px;top:746px;width:306px;font-size:9px;line-height:17.6px;color:var(--muted)}
.services{left:430px;top:610px;list-style:none;font-size:8.6px;color:#222}
.services li{height:24px;display:flex;align-items:center}
.services li::before{content:"\2192";color:#666;font-size:8px;margin-right:8px}
.news-item{left:632px;width:180px}
.cal{position:absolute;left:0;top:0;width:21px;text-align:center;font-size:8px;color:#333}
.cal .box{width:20px;height:19px;border:2px solid var(--red);border-top-width:5px;border-radius:2px;font-size:7px;font-weight:700;line-height:12px;margin-bottom:2px}
.news-body{position:absolute;left:29px;top:0;width:150px;font-size:8.2px;line-height:12.8px;color:#444}
.news-body h4{font-size:8.4px;line-height:11.2px;color:#111;margin-bottom:5px}
.news-body a{color:var(--red);text-decoration:none}

/* partners */
.partners{left:28px;top:870px;width:858px;height:94px;border-top:1px solid var(--rule);border-bottom:1px solid var(--rule);box-shadow:0 2px 4px rgba(0,0,0,.06)}
.partner-row{left:112px;top:904px;width:690px;display:flex;justify-content:space-between;align-items:center}
.partner{font-family:"PT Sans Narrow",sans-serif;font-weight:700;font-size:13px;color:#555}

/* footer */
.footer{left:0;top:989px;width:914px;height:171px;background:var(--footer)}
.footer h3{position:absolute;top:18px;font-family:"PT Sans Narrow",sans-serif;font-weight:400;font-size:15px;color:var(--footer-head)}
.footer-links{position:absolute;top:45px;list-style:none;font-family:"PT Sans Narrow",sans-serif;font-size:9.5px;color:var(--footer-text)}
.footer-links li{height:20px}
.divider{position:absolute;top:21px;width:1px;height:138px;background:#444}
.tweet{position:absolute;left:410px;width:210px;font-family:"PT Sans Narrow",sans-serif;font-size:9.5px;line-height:16px;color:var(--footer-text)}
.tweet small{display:block;color:#888;font-size:9px;margin-top:3px}
.social{position:absolute;left:672px;top:40px;list-style:none;font-family:"PT Sans Narrow",sans-serif;font-style:italic;font-size:9.5px;color:var(--footer-text)}
.social li{height:26.4px;display:flex;align-items:center}
.social li::before{content:"";flex:none;width:21px;height:21px;border-radius:50%;background:var(--icon);margin-right:11px}
.base{left:0;top:1160px;width:914px;height:40px;background:var(--footer-base)}
.copy{left:110px;top:16px;font-size:8.5px;color:#888;font-family:"PT Sans Narrow",sans-serif}
.badge{left:704px;top:5px;width:102px;height:32px;background:#fff;border-radius:4px}
.code{left:815px;top:15px;font-size:9px;color:#ddd}
</style>
</head>
<body>

<div class="abs account-links">My Account<i>/</i>Register<i>/</i>Log In<i>/</i>Wish List</div>
<div class="abs lang"><span class="flag"></span>ENGLISH<span class="caret">&#9662;</span></div>
<div class="abs search">Search
  <svg width="10" height="10" viewBox="0 0 10 10"><circle cx="4" cy="4" r="3" fill="none" stroke="#666" stroke-width="1.3"/><line x1="6.2" y1="6.2" x2="9.5" y2="9.5" stroke="#666" stroke-width="1.5"/></svg>
</div>
<div class="abs brand">QUILLBROOK<small>ADVISORY</small></div>

<nav class="abs mainnav">
  <a style="left:118px">ABOUT US</a>
  <a style="left:190px">SERVICES</a>
  <a style="left:258px">WORKING WITH US</a>
  <a style="left:366px">CONTACT US</a>
  <a style="left:448px">LINKS</a>
  <a style="left:501px">TESTIMONIALS</a>
  <a style="left:592px">NEWS</a>
  <a style="left:644px">ARTICLE OF THE MOMENT ARCHIVE</a>
</nav>

<div class="abs hero" role="img" aria-label="Photo of an advisor in a black dress walking along a sunny waterfront promenade"></div>
<h1 class="abs hero-title"><span>Quillbrook</span>Advisory</h1>
<div class="abs dots"><b></b><b></b><b></b><b></b></div>

<h2 class="abs section-head" style="left:107px;top:489px">Getting to know Quillbrook Advisory</h2>
<p class="abs intro-text">Quillbrook Advisory aims to service the needs of its clients by focusing on the present rather than reporting on historical figures. We recognise that business owners benefit from regular contact with their accountant.</p>
<div class="abs btn" style="left:696px;top:517px;width:110px;height:29px;font-size:11px">VIEW MORE</div>

<h2 class="abs section-head" style="left:109px;top:581px">Quillbrook Advisory Difference</h2>
<h2 class="abs section-head" style="left:430px;top:580px">Our Services List</h2>
<h2 class="abs section-head" style="left:631px;top:581px">Latest News</h2>

<div class="abs photo" role="img" aria-label="Photo of an advisor in a red dress standing on a marina jetty beside boats"></div>
<p class="abs diff-text">Not all Accountants are created equally … the Quillbrook Advisory difference Quillbrook Advisory takes pride in not following the status quo, the following points are just some of the unique benefits you will experience when working with us. Believing in the here and now: A proactive accountant that focuses on providing timely and relevant information.</p>

<ul class="abs services">
  <li>Assistance with ABN &amp; GST Registrations</li>
  <li>Determining Record Keeping requirements</li>
  <li>Establishing suitable accounting systems</li>
  <li>Analysis of business start up costs</li>
  <li>Preparation of income and expense budget</li>
  <li>Calculating break-even point</li>
  <li>Management of Cash Flow</li>
  <li>Industry Benchmarking</li>
  <li>Profit &amp; Loss Analysis</li>
  <li>Monthly reporting on business performance</li>
</ul>

<div class="abs news-item" style="top:614px">
  <div class="cal"><div class="box">16</div>OCT</div>
  <div class="news-body"><h4>Fly lines to cover every saltwater fly fishing situatio</h4>Fly lines to cover every saltwater fly fishing situation from Riva, Regal Fin, Carrow, Precise Casters<br><a>Read more...</a></div>
</div>
<div class="abs news-item" style="top:708px">
  <div class="cal"><div class="box">15</div>OCT</div>
  <div class="news-body"><h4>Fly lines to cover every saltwater fly fishing situatio</h4>Fly lines to cover every saltwater fly fishing situation from Riva, Regal Fin, Carrow, Precise Casters<br><a>Read more...</a></div>
</div>
<div class="abs btn" style="left:632px;top:810px;width:71px;height:27px;font-size:9px;font-family:Arimo,sans-serif;font-weight:400;border-radius:0">VIEW ALL</div>

<div class="abs partners"></div>
<div class="abs partner-row">
  <span class="partner">Verabyte</span>
  <span class="partner">Northgrain</span>
  <span class="partner">Kestrel Data</span>
  <span class="partner">Halloway Supply</span>
  <span class="partner">Corvel</span>
  <span class="partner">Tidemark</span>
  <span class="partner">Brightwell</span>
  <span class="partner">Lumen Arc</span>
</div>

<footer class="abs footer">
  <h3 style="left:145px">COMPANY</h3>
  <ul class="footer-links" style="left:145px"><li>COMPANY OVERVIEW</li><li>ABOUT US</li><li>SERVICES PROVIDE</li><li>OUR PROCESS</li><li>OUR CLIENTS</li></ul>
  <span class="divider" style="left:254px"></span>
  <h3 style="left:278px">WHAT WE DO</h3>
  <ul class="footer-links" style="left:278px"><li>VALUE PROPOSITION</li><li>OUR WORK</li><li>TESTIMONIALS</li><li>FAQ</li><li>CONTACT US</li></ul>
  <span class="divider" style="left:385px"></span>
  <h3 style="left:410px">SOCIAL FEED</h3>
  <p class="tweet" style="top:40px">Nunc tempus felis vitae urna. Vivamus porttitor, g, purus nisi eleifend libero, a tempus<small>Posted 3 hours ago</small></p>
  <p class="tweet" style="top:102px">Nunc tempus felis vitae urna. Vivamus porttitor, g, purus nisi eleifend libero, a tempus<small>Posted 3 hours ago</small></p>
  <span class="divider" style="left:635px"></span>
  <h3 style="left:670px">GET CONNECTED</h3>
  <ul class="social"><li>Friendwall</li><li>Chirpline</li><li>Netlink Pro</li><li>RSS</li></ul>
</footer>

<div class="abs base">
  <p class="abs copy">© 2013 Company Name.&nbsp; All right reserved.&nbsp; Term of Use</p>
  <div class="abs badge" aria-label="Professional membership badge"></div>
  <span class="abs code">C1</span>
</div>

</body>
</html>
```